Student project platform needs an awareness flyer

Tornuvel is a matchmaking and crowdfunding site for student projects. On this platform, students can team up with each other to invent a new product, innovate, or start a business. They can also raise funds for their project.

** I am in need of an 8x11" flyer to print and distribute digitally which notifies students of all different skill sets that this site exists.

The flyer should communicate that a diverse user base is being built on this site, with people who have skills in programming, engineering, design, business, finance, and so on.

The flyer should also be clean and modern, with an emphasis on creativity and innovation. I've attached the business' logo to give you an idea of the artistic style we have already established.

Target Market(s)

University students

Industry/Entity Type

Crowdfunding

Font styles to use
Serif
Sans Serif

Requirements
Must have
• * Clean and modern design
• * Color scheme of my logo: #336699 and #669933 (blue and green)
• * Convey that this site is for people of different skill sets: programming, engineering, design, business, finance, and so on.
• * See the attached "Tornuvel Copy.txt" for text to include on the flyer

```html
<!DOCTYPE html>
<html lang="en">
<head>
<meta charset="utf-8">
<title>Tornuvel Flyer</title>
<link rel="stylesheet" href="https://fonts.googleapis.com/css2?family=Mulish:wght@400;600;700&family=Roboto:wght@400;500&display=swap">
<style>
  :root {
    --stage: #1f1f1f;
    --brand-blue: #336699;
    --brand-green: #669933;
    --paper: #ffffff;
    --mist: #e9e9ea;
    --body-text: #4d4d4f;
  }
  * { margin: 0; padding: 0; box-sizing: border-box; }
  html, body {
    width: 1200px; height: 1200px; overflow: hidden;
    background: var(--stage);
    font-family: "Mulish", sans-serif;
  }
  .flyer {
    position: absolute; left: 238px; top: 103px;
    width: 724px; height: 994px;
    background: var(--paper);
    overflow: hidden;
  }
  .masthead {
    position: absolute; left: 0; top: 0; width: 100%; height: 162px;
    background: linear-gradient(135deg, #ffffff 0%, #ececed 45%, #f7f7f7 70%, #e6e6e7 100%);
    display: flex; flex-direction: column; align-items: center; justify-content: center; gap: 10px;
  }
  .brand-dot {
    width: 52px; height: 52px; border-radius: 50%;
    background: var(--brand-blue);
  }
  .brand-name {
    font-size: 30px; font-weight: 600; letter-spacing: 1px;
    color: var(--brand-blue);
  }
  .hero-photo {
    position: absolute; left: 0; top: 167px; width: 100%; height: 364px;
    background: linear-gradient(160deg, #8fa7a0 0%, #c9b7a4 40%, #a46a5c 70%, #6f6358 100%);
  }
  .callout-band {
    position: absolute; left: 0; top: 531px; width: 100%; height: 75px;
    background: var(--brand-blue); color: #fff;
    font-family: "Roboto", sans-serif; text-align: center;
    display: flex; flex-direction: column; justify-content: center;
  }
  .callout-band .lead { font-size: 22px; font-weight: 400; line-height: 27px; }
  .callout-band .strong { font-size: 22px; font-weight: 500; line-height: 27px; }
  .details {
    position: absolute; left: 0; top: 611px; width: 100%; height: 383px;
    background: linear-gradient(180deg, #e4e4e5 0%, #f2f2f2 45%, #ffffff 85%);
  }
  .join-hex { position: absolute; left: 66px; top: 653px; width: 238px; height: 273px; }
  .join-text {
    position: absolute; left: 66px; top: 716px; width: 238px;
    text-align: center; color: #fff;
    font-size: 21px; line-height: 27px;
  }
  .about-title {
    position: absolute; left: 359px; top: 670px;
    font-size: 19px; font-weight: 700; color: var(--brand-green);
  }
  .about-rule {
    position: absolute; left: 350px; top: 708px; width: 30px; height: 2px;
    background: var(--brand-blue);
  }
  .about-copy {
    position: absolute; left: 359px; top: 720px; width: 320px;
    font-size: 18.4px; line-height: 27.6px; color: var(--body-text);
  }
  .footer-band {
    position: absolute; left: 0; top: 982px; width: 100%; height: 12px;
    background: var(--brand-blue);
  }
  .visit-button {
    position: absolute; left: 359px; top: 943px; width: 302px; height: 51px;
    background: var(--brand-green); color: #fff;
    clip-path: polygon(0 0, 290px 0, 302px 11px, 302px 100%, 0 100%);
    font-size: 18px; display: flex; align-items: center; justify-content: center;
  }
</style>
</head>
<body>
  <main class="flyer">
    <header class="masthead">
      <div class="brand-dot"></div>
      <div class="brand-name">TORNUVEL</div>
    </header>

    <div class="hero-photo" role="img" aria-label="Photo of a diverse group of smiling students joining hands in a high five over a desk"></div>

    <section class="callout-band">
      <p class="lead">Calling all students who want to</p>
      <p class="strong">Build, innovate, invent, or start a business</p>
    </section>

    <section class="details"></section>

    <svg class="join-hex" viewBox="0 0 238 273" aria-hidden="true">
      <polygon points="119,0 238,68 238,204 119,273 0,204 0,68" fill="#669933"/>
      <polygon points="119,11 228,74 228,198 119,262 10,198 10,74" fill="none" stroke="#ffffff" stroke-width="1.2"/>
    </svg>
    <p class="join-text">Join Tornuvel<br>to support<br>and lend your<br>skills to<br>student projects!</p>

    <h2 class="about-title">What is Tornuvel?</h2>
    <div class="about-rule"></div>
    <p class="about-copy">Tornuvel is a matchmaking and crowdfunding platform for student projects. It allows students to form teams of diverse skills and raise money to build, innovate, invent, or start a business.</p>

    <div class="footer-band"></div>
    <a class="visit-button">Visit www.Tornuvel.com</a>
  </main>
</body>
</html>
```